Label Design for a New Alcoholized Root Beer

Create a design for a new alcoholized root beer. This is a new product category in the USA growing very rapidly. Root Beer is a popular flavor of Cola, but recently, beer manufacturers have added alcohol to it and have created a new product that has gained traction on the market at a tremendous rate.

Root Beer is vintage product that has been around for a hundred years. Consumers of this product are mostly male between the age of 30 to 45. They purchase this product for its nostalgia and vintage look and taste.

This product will be in a standard 355 mL brown bottle.

It is 5.9% abv.

The name of the product is ''Corvel's Hard Root Beer''.

We have uploaded some pictures of traditional root beers to give you an idea of the feel we want our product to have and also, the bottle the product will be filled in.

Target Market(s)

Consumers are male 30-45, same market as craft beer consumers

Industry/Entity Type

Product

Requirements
Must have
• Design must have a vintage feel to it

```html
<!DOCTYPE html>
<html lang="en">
<head>
<meta charset="UTF-8">
<title>Corvel's Hard Root Beer – Label</title>
<link rel="stylesheet" href="https://fonts.googleapis.com/css2?family=Rye&family=Roboto+Condensed:wght@300;700&display=swap">
<style>
  :root {
    --canvas: #ffffff;
    --label-brown: #714c2b;
    --label-edge: #d9c39a;
    --title-yellow: #f6e51b;
    --ink-white: #ffffff;
    --medallion: #0b0b0b;
    --medallion-rim: #c9a35e;
    --drink-light: #f1cf7a;
    --drink-dark: #b9761f;
  }
  html, body {
    margin: 0;
    padding: 0;
    width: 1200px;
    height: 1000px;
    overflow: hidden;
    background: var(--canvas);
  }
  .canvas {
    position: relative;
    width: 1200px;
    height: 1000px;
  }
  .bottle-label {
    position: absolute;
    left: 386px;
    top: 157px;
    width: 427px;
    height: 685px;
  }
  .label-body {
    fill: var(--label-brown);
    stroke: var(--label-edge);
    stroke-width: 1.2;
  }
  .label-inner-line {
    fill: none;
    stroke: var(--label-edge);
    stroke-width: 0.6;
    stroke-dasharray: 1.5 1.5;
  }
  .label-star { fill: var(--ink-white); }
  .brand-name {
    font-family: "Rye", serif;
    font-size: 50px;
    fill: var(--title-yellow);
  }
  .medallion-rim { fill: var(--medallion-rim); }
  .medallion { fill: var(--medallion); }
  .product-type {
    font-family: "Roboto Condensed", sans-serif;
    font-weight: 700;
    font-size: 31px;
    letter-spacing: -0.5px;
    fill: var(--ink-white);
  }
  .volume {
    font-family: "Roboto Condensed", sans-serif;
    font-weight: 300;
    font-size: 16px;
    letter-spacing: 1px;
    fill: var(--ink-white);
  }
</style>
</head>
<body>
<main class="canvas">
  <svg class="bottle-label" viewBox="0 0 267 428" xmlns="http://www.w3.org/2000/svg" aria-label="Corvel's Hard Root Beer label">
    <defs>
      <linearGradient id="drinkGradient" x1="0" y1="0" x2="0" y2="1">
        <stop offset="0" stop-color="#f4efe2"/>
        <stop offset="0.25" stop-color="var(--drink-light)"/>
        <stop offset="1" stop-color="var(--drink-dark)"/>
      </linearGradient>
      <path id="productArc" d="M30,322 Q134,386 240,322"/>
    </defs>

    <path class="label-body"
      d="M134,2 L205,28 L247,28 L247,210 L255,210 Q267,210 267,222 L267,416 Q267,427 255,427 L12,427 Q1,427 1,416 L1,222 Q1,210 13,210 L20,210 L20,28 L62,28 Z"/>
    <path class="label-inner-line"
      d="M134,6 L204,32 L243,32 L243,214 L255,214 Q263,214 263,222 L263,416 Q263,423 255,423 L12,423 Q5,423 5,416 L5,222 Q5,214 13,214 L24,214 L24,32 L63,32 Z"/>

    <polygon class="label-star"
      points="134,35 138.7,46.5 151,47.3 141.5,55.2 144.6,67.2 134,60.6 123.4,67.2 126.5,55.2 117,47.3 129.3,46.5"/>

    <text class="brand-name" x="134" y="140" text-anchor="middle" textLength="190" lengthAdjust="spacingAndGlyphs">CORVEL'S</text>

    <circle class="medallion-rim" cx="134" cy="242" r="73"/>
    <circle class="medallion" cx="134" cy="242" r="70"/>
    <g role="img" aria-label="Photo of a frosted glass mug filled with root beer">
      <rect x="104" y="188" width="62" height="100" rx="8" fill="url(#drinkGradient)"/>
    </g>

    <text class="product-type">
      <textPath href="#productArc" startOffset="50%" text-anchor="middle">Hard Root Beer</textPath>
    </text>

    <text class="volume" x="134" y="407" text-anchor="middle">xx ml</text>
  </svg>
</main>
</body>
</html>
```